Brightwater Health Partners, LLC Business Card update!

would like a classier business card. Our cards currently just have our logo and contact information. Need better use of color and creativity
Logo attached.

Target Market(s)

Potential clients, contacts, existing clients. We are a consulting company

Industry/Entity Type

Business

Contact Information for Business Card

We like our colors but just have a boring card with our logo and a white background. I want something that stands out.

Colors
ec1f27
757575

Requirements
Must have
• Color to stay consistent. Logo provided
Nice to have
• Just better use of color/ design

```html
<!DOCTYPE html>
<html lang="en">
<head>
<meta charset="utf-8">
<title>Brightwater Health Partners – Business Card</title>
<link href="https://fonts.googleapis.com/css2?family=Exo+2:wght@400;600&display=swap" rel="stylesheet">
<style>
  :root {
    --brand-pink: #d8176b;
    --brand-grey: #757575;
    --card-white: #ffffff;
    --backdrop: #e6e6e6;
    --ink-light: #ffffff;
  }
  * { box-sizing: border-box; margin: 0; padding: 0; }
  html, body {
    width: 1200px; height: 901px; overflow: hidden;
    background: var(--backdrop);
    font-family: "Exo 2", "Trebuchet MS", sans-serif;
  }
  .stage {
    width: 1200px; height: 901px;
    display: flex; align-items: center; justify-content: center; gap: 50px;
  }
  .card {
    position: relative;
    width: 540px; height: 310px;
    border-radius: 30px;
    overflow: hidden;
    background: var(--card-white);
    box-shadow: 0 0 0 6px #cfcfcf, 0 14px 30px rgba(0,0,0,0.18);
  }
  .card-shape { position: absolute; inset: 0; }

  .wordmark { position: absolute; display: flex; align-items: center; gap: 12px; color: var(--brand-pink); font-weight: 400; }
  .wordmark-dot { border-radius: 50%; background: var(--brand-pink); flex: none; }
  .wordmark-name { line-height: 1.05; }
  .wordmark-name span { display: block; }

  .front .wordmark { left: 34px; top: 46px; font-size: 22px; }
  .front .wordmark-dot { width: 26px; height: 26px; }
  .front .wordmark-name span + span { font-size: 15px; }

  .contact-block {
    position: absolute; right: 34px; top: 104px;
    text-align: right; color: var(--ink-light);
  }
  .person-name { font-size: 19px; font-weight: 600; letter-spacing: 1.5px; }
  .person-role { font-size: 13px; margin-top: 2px; }
  .address { font-size: 13px; margin-top: 14px; line-height: 1.35; }
  .contact-list { list-style: none; margin-top: 14px; font-size: 12.5px; }
  .contact-list li { display: flex; justify-content: flex-end; align-items: center; gap: 8px; line-height: 1.55; }
  .contact-list svg { width: 12px; height: 12px; fill: var(--ink-light); flex: none; }

  .back .wordmark { right: 56px; bottom: 58px; font-size: 30px; }
  .back .wordmark-dot { width: 34px; height: 34px; }
  .back .wordmark-name span + span { font-size: 20px; }
</style>
</head>
<body>
<main class="stage">

  <section class="card front" aria-label="Business card front">
    <svg class="card-shape" viewBox="0 0 540 310" preserveAspectRatio="none" aria-hidden="true">
      <path d="M250,0 C190,90 190,220 230,310 L540,310 L540,0 Z" fill="var(--brand-grey)"/>
      <path d="M268,0 C208,90 208,220 248,310 L540,310 L540,0 Z" fill="var(--brand-pink)"/>
    </svg>

    <div class="wordmark">
      <span class="wordmark-dot"></span>
      <p class="wordmark-name"><span>BRIGHTWATER</span><span>Health Partners</span></p>
    </div>

    <div class="contact-block">
      <p class="person-name">DANIEL WHITMORE</p>
      <p class="person-role">Managing Director</p>
      <p class="address">214 Harbor View Suite 9<br>Eastgate</p>
      <ul class="contact-list">
        <li>012 555 0147
          <svg viewBox="0 0 12 12"><path d="M2.5 1l2 2-1 1.5a7 7 0 0 0 4 4L9 7.5l2 2L9.5 11A9 9 0 0 1 1 2.5z"/></svg></li>
        <li>012 555 0148
          <svg viewBox="0 0 12 12"><path d="M3 0h6a1 1 0 0 1 1 1v10a1 1 0 0 1-1 1H3a1 1 0 0 1-1-1V1a1 1 0 0 1 1-1zm0 2v7h6V2z"/></svg></li>
        <li>012 555 0149
          <svg viewBox="0 0 12 12"><path d="M3 0h5l2 2v3H3zM1 5h10v6H1zm2 2v1h2V7zm4 0v1h2V7z"/></svg></li>
        <li>hello@brightwaterhp.com
          <svg viewBox="0 0 12 12"><path d="M0 2h12v8H0zm1 1v.5l5 3.5 5-3.5V3z"/></svg></li>
        <li>www.brightwaterhealth.net
          <svg viewBox="0 0 12 12"><circle cx="6" cy="6" r="5.5"/></svg></li>
      </ul>
    </div>
  </section>

  <section class="card back" aria-label="Business card back">
    <div class="wordmark">
      <span class="wordmark-dot"></span>
      <p class="wordmark-name"><span>BRIGHTWATER</span><span>Health Partners</span></p>
    </div>
  </section>

</main>
</body>
</html>
```